Talvor GmbH business card

We Talvor GmbH based in Switzerland are looking for a business card design. The Fresh Jung, appealing to customers of all kinds. We already have a logo to upload but still a business card. Details: Talvor GmbH Address: Lindenweg 14b in 9476 Brugwil. Tel: 41 79 462 37 18, web: Talvor.ch, E-mail: info@Talvor.ch Facebook: Talvor GmbH. I am the Managing Director: Luka Petrovac. On reverse: Title: Transporter and bus rental Gross: Without deposit Super prices
Contact Information for Business Card
Siehe Projektbeschreibung
Requirements
Should not have
- Other pictures

```html
<!DOCTYPE html>
<html lang="de">
<head>
<meta charset="utf-8">
<title>Talvor GmbH – Visitenkarte</title>
<link rel="stylesheet" href="https://fonts.googleapis.com/css2?family=Lato:wght@400;700;900&display=swap">
<style>
  :root {
    --navy: #0b0b80;
    --steel: #7f9cc0;
    --paper: #ffffff;
    --stage: #e4e4e6;
    --ink: #14143a;
  }
  * { box-sizing: border-box; margin: 0; padding: 0; }
  html, body { width: 1200px; height: 680px; overflow: hidden; }
  body {
    background: var(--stage);
    font-family: "Lato", sans-serif;
    display: flex;
    align-items: center;
    justify-content: center;
    gap: 40px;
  }
  .card {
    position: relative;
    width: 520px;
    height: 336px;
    overflow: hidden;
    box-shadow: 0 6px 18px rgba(0,0,0,0.18);
  }
  .card-front { background: var(--paper); color: var(--ink); }
  .front-shapes { position: absolute; inset: 0; }
  .brand {
    position: absolute; left: 40px; top: 70px;
    display: flex; align-items: center; gap: 14px;
  }
  .brand-square { width: 40px; height: 40px; background: var(--navy); }
  .brand-name {
    font-weight: 900; font-size: 40px; color: var(--navy);
    letter-spacing: 1px;
  }
  .holder {
    position: absolute; right: 40px; top: 128px; text-align: right;
  }
  .holder-name { font-size: 22px; color: var(--navy); font-weight: 400; }
  .holder-role { font-size: 12px; color: var(--ink); margin-top: 1px; }
  .contact {
    position: absolute; left: 40px; top: 200px;
    list-style: none; font-size: 13px; line-height: 19px;
  }
  .contact li { display: flex; align-items: center; gap: 10px; }
  .contact svg { width: 12px; height: 12px; fill: var(--navy); flex: none; }
  .address {
    position: absolute; right: 40px; top: 198px;
    text-align: right; font-size: 13px; line-height: 17px;
  }
  .website {
    position: absolute; right: 28px; bottom: 22px;
    color: var(--paper); font-size: 13px; letter-spacing: 0.3px;
  }
  .card-back {
    background: var(--navy);
    display: flex; flex-direction: column; align-items: center; justify-content: center;
    text-align: center;
  }
  .offer {
    color: var(--steel); font-weight: 700; font-size: 44px;
    line-height: 52px; letter-spacing: 1.5px;
  }
  .service {
    margin-top: 34px; color: #e8ecf6; font-size: 21px; letter-spacing: 0.5px;
  }
</style>
</head>
<body>
  <section class="card card-front" aria-label="Vorderseite">
    <svg class="front-shapes" viewBox="0 0 520 336" aria-hidden="true">
      <line x1="40" y1="186" x2="480" y2="186" stroke="#0b0b80" stroke-width="1"/>
      <path d="M 20 336 C 170 292 320 254 470 244 C 330 264 190 300 70 336 Z" fill="#7f9cc0"/>
      <path d="M 70 336 C 210 300 360 272 520 262 L 520 336 Z" fill="#0b0b80"/>
    </svg>

    <div class="brand">
      <span class="brand-square"></span>
      <span class="brand-name">Talvor</span>
    </div>

    <div class="holder">
      <p class="holder-name">Luka Petrovac</p>
      <p class="holder-role">Geschäftsführer</p>
    </div>

    <ul class="contact">
      <li>
        <svg viewBox="0 0 12 12"><path d="M2.4 0.8 4 0.4 5.2 3 4.1 4c.6 1.5 1.8 2.7 3.3 3.3l1-1.1 2.6 1.2-.4 1.6C10.3 10.8 9 11.4 7.6 11 4.4 10 1.9 7.5 1 4.3.6 2.9 1.2 1.6 2.4.8Z"/></svg>
        +41 79 462 37 18
      </li>
      <li>
        <svg viewBox="0 0 12 12"><path d="M0 2h12v8H0Z M1 3v.3l5 3.4 5-3.4V3Z" fill-rule="evenodd"/></svg>
        info@Talvor.ch
      </li>
      <li>
        <svg viewBox="0 0 12 12"><rect x="1" y="1" width="10" height="10"/></svg>
        /Talvor-GmbH
      </li>
    </ul>

    <address class="address" style="font-style: normal;">
      Lindenweg 14b<br>9476 Brugwil
    </address>

    <p class="website">www.Talvor.ch</p>
  </section>

  <section class="card card-back" aria-label="Rückseite">
    <p class="offer">Ohne Kaution</p>
    <p class="offer">Super Preise</p>
    <p class="service">Transporter und Bus Vermietung</p>
  </section>
</body>
</html>
```